Alder Court Parking Lot Flyer

I need a 1/2 page flyer to look and feel like my website. With all the relevant information like phone # and map to our office. It needs to look and feel like a shortened or brief version of our website but on paper. I would like the colors to be the same palette as the website and I would like the flyer to be full color front and back. The web address is pinonridgelegalteam.com
Our logo is on the website and all relevant information can be viewed there as well. Please include our web address on the flyer as well.
This is for a Law Firm so it needs to be very PROFESSIONAL Looking.
DO NOT USE OUR PHOTOGRAPHS OR PICTURES OF US.

Target Market(s)

People visiting the courthouse who need to hire a criminal defense attorney immediately.

Industry/Entity Type

Court

Font styles to use
Serif

Colors

Designer to choose colors to be used in the design.

Requirements
Must have
• Contact information and map. Web address is crucial as well.

```html
<!DOCTYPE html>
<html lang="en">
<head>
<meta charset="utf-8">
<title>Piñon Ridge Legal Team – Alder Court Flyer</title>
<link href="https://fonts.googleapis.com/css2?family=Bree+Serif&family=Cormorant+Garamond:wght@500&family=Noto+Serif:wght@400;700&family=Bitter:wght@700;800&display=swap" rel="stylesheet">
<style>
  :root{
    --ink:#1f1f1f;
    --black:#222222;
    --gold:#9b8556;
    --gold-light:#b49a62;
    --paper:#ebebeb;
    --white:#f7f7f7;
    --sky:#49b4e6;
    --stage:#cfcfcf;
    --text:#1c1c1c;
  }
  *{box-sizing:border-box;margin:0;padding:0}
  html,body{width:1200px;height:927px;overflow:hidden}
  body{background:var(--stage);position:relative;font-family:"Noto Serif",serif;color:var(--text)}
  .side-label{position:absolute;font-family:"Bitter",serif;font-weight:800;font-size:14px;color:#111;letter-spacing:.5px}
  .abs{position:absolute}

  /* FRONT */
  .front{position:absolute;left:75px;top:88px;width:515px;height:667px;background:var(--paper);overflow:hidden;box-shadow:0 4px 10px rgba(0,0,0,.35)}
  .front .top-band{left:0;top:0;width:100%;height:15px;background:var(--gold)}
  .front .masthead{left:0;top:15px;width:100%;height:72px;background:var(--black)}
  .brand-mark{position:absolute;left:24px;top:17px;width:38px;height:38px;border:1.5px solid #d8d8d8;border-radius:50%}
  .brand-name{position:absolute;left:87px;top:17px;font-family:"Cormorant Garamond",serif;font-weight:500;font-size:20px;line-height:20px;letter-spacing:1.2px;color:#e4e4e4;text-transform:uppercase}
  .front .rule-top{left:0;top:87px;width:100%;height:5px;background:var(--gold)}
  .hero{left:0;top:92px;width:100%;height:132px;background:linear-gradient(90deg,#2a2117 0%,#6a5334 30%,#a8895a 55%,#4a3a26 80%,#1d1711 100%)}
  .tagline{position:absolute;left:0;right:0;top:179px;text-align:center;font-family:"Cormorant Garamond",serif;font-weight:500;font-size:17px;color:#fff;letter-spacing:.4px;text-transform:uppercase}
  .tagline b{font-family:"Bree Serif",serif;font-weight:400;font-size:21px}
  .front .rule-bottom{left:0;top:224px;width:100%;height:8px;background:var(--gold)}
  .pill{position:absolute;height:20px;padding:0 7px;background:var(--sky);border-radius:3px;color:#fff;font-family:"Bitter",serif;font-weight:700;font-size:10.5px;line-height:20px;box-shadow:0 1px 2px rgba(0,0,0,.25)}
  .body-copy{position:absolute;left:16px;width:486px;font-size:8.6px;line-height:10.9px;text-align:justify}
  .body-copy p{margin-bottom:10.9px}
  .body-copy h3{font-size:8.7px;font-weight:700}
  .practice{position:absolute;top:512px;font-size:8.6px;line-height:10.9px;list-style:none}
  .practice li{position:relative;padding-left:15px}
  .practice li::before{content:"";position:absolute;left:2px;top:3.5px;width:4px;height:4px;border-radius:50%;background:var(--text)}
  .practice li.cont::before{display:none}
  .front-foot{left:0;top:612px;width:515px;height:55px}
  .web-front{position:absolute;right:14px;bottom:12px;font-family:"Bree Serif",serif;font-size:12.5px;letter-spacing:1px;color:var(--gold-light)}

  /* BACK */
  .back{position:absolute;left:640px;top:113px;width:512px;height:665px;background:var(--white);overflow:hidden;box-shadow:0 4px 10px rgba(0,0,0,.35)}
  .back .spine{left:0;top:0;width:208px;height:100%;background:var(--black)}
  .back .stripe{left:28px;top:0;width:12px;height:100%;background:var(--gold)}
  .photo-suit{left:40px;top:44px;width:168px;height:368px;background:linear-gradient(180deg,#2b3340 0%,#1d2229 45%,#3a2a22 75%,#20242a 100%)}
  .photo-paper{left:40px;top:420px;width:168px;height:180px;background:linear-gradient(160deg,#f2f2f2 0%,#d9d9d9 55%,#9c9c9c 100%)}
  .case-list{position:absolute;left:218px;top:95px;width:282px;font-size:8.5px;line-height:10.8px;text-align:justify}
  .case-list .sub{font-family:"Bitter",serif;font-weight:700;color:var(--gold);font-size:9px;margin:-20px 0 11px}
  .case{margin-bottom:18px}
  .case h4{font-family:"Bitter",serif;font-weight:800;font-size:8.6px;line-height:10.6px}
  .contact-copy{position:absolute;left:218px;top:471px;width:282px;font-size:8.5px;line-height:10.8px}
  .map-card{left:218px;top:507px;width:280px;height:97px;background:var(--black);border:3px solid var(--gold)}
  .map-area{position:absolute;right:0;top:0;width:148px;height:100%;background:linear-gradient(135deg,#1b1b1b,#2a2a2a)}
  .map-pin{position:absolute;left:195px;top:40px;width:16px;height:16px;background:var(--gold)}
  .map-text{position:absolute;left:6px;top:5px;font-family:"Bree Serif",serif;font-size:11px;line-height:11.5px;color:var(--gold-light)}
  .map-phone{position:absolute;left:6px;top:66px;display:flex;align-items:center;gap:7px;font-family:"Bree Serif",serif;font-size:13.5px;color:var(--gold-light)}
  .web-back{position:absolute;left:218px;width:282px;top:624px;text-align:center;font-family:"Bree Serif",serif;font-size:13px;letter-spacing:.6px;color:var(--gold-light)}
</style>
</head>
<body>
  <div class="side-label" style="left:304px;top:37px">FRONT</div>
  <div class="side-label" style="left:871px;top:86px">BACK</div>

  <section class="front">
    <div class="abs top-band"></div>
    <header class="abs masthead">
      <span class="brand-mark"></span>
      <div class="brand-name">Piñon Ridge Legal<br>Team</div>
    </header>
    <div class="abs rule-top"></div>
    <div class="abs hero" role="img" aria-label="Photo of a shelf of leather-bound law books"></div>
    <div class="tagline">Clearing your name is our <b>#1</b> priority</div>
    <div class="abs rule-bottom"></div>

    <div class="pill" style="left:16px;top:242px">About Us</div>
    <div class="body-copy" style="top:265px">
      <p>Since 1997, Piñon Ridge Legal Team in Albuquerque has focused on protecting the rights of our clients. We employ bold strategies and aggressive representation to achieve these goals. Our firm consists of two attorneys who are committed to success for our clients, and a dedicated staff working collectively work to achieve these goals.</p>
      <h3>We offer a free initial consultation</h3>
      <p>The experienced trial lawyers at our firm represent clients in all criminal law areas in Federal Court, State District Court, Magistrate and Municipal Courts in all Counties of New Mexico. Our firm prepares all cases for trial. It is our years of courtroom experience with the specific charges our clients face distinguish our firm.</p>
      <h3>Personalized Legal Representation-Our Strategy for Success:</h3>
      <p>Each case is unique and each client receives our full attention to conduct a thorough investigation, and fulfill all procedural and evidentiary rights. We require the prosecution to assume to full burden of proof in each case. Our record of competency and preparedness commands the respect of prosecutors and judges.</p>
      <p>Our goal is to do everything possible to achieve favorable results for our clients.</p>
      <p>Among the numerous cases reported in the media which the firm has handled, Mr. Varela and Mr. Castellan represented a client in Federal Court in 2012 in the Country's largest Healthcare Fraud and Conspiracy case. The case was featured on Channel 7 News and regional and national networks, and internationally by international news services and wire agencies.</p>
    </div>

    <div class="pill" style="left:16px;top:488px">Practice Areas</div>
    <ul class="practice" style="left:16px">
      <li>Larceny</li><li>Drug Trafficking</li><li>Minor in Possession</li><li>Child Molestation</li><li>Child Pornography</li><li>Sex Crimes</li><li>Serious Drug Charges:</li><li class="cont">Heroin, Cocaine, &amp; Methamphetamine</li><li>Marijuana</li>
    </ul>
    <ul class="practice" style="left:218px">
      <li>Probation Violations</li><li>Federal Drug Crimes</li><li>Resisting Arrest, Public Affray</li><li>White Collar Crimes</li><li>Homicide, Attempted Murder Attorney</li><li>Assault &amp; Battery</li><li>Robbery, Burglary, and Theft</li><li>Domestic Violence</li><li>DUI/DWI Defense</li>
    </ul>

    <svg class="abs front-foot" viewBox="0 0 515 55" aria-hidden="true">
      <polygon points="0,0 515,10 515,55 0,55" fill="#9b8556"/>
      <polygon points="0,14 515,8 515,55 0,55" fill="#222222"/>
    </svg>
    <div class="web-front">www.pinonridgelegalteam.com</div>
  </section>

  <section class="back">
    <div class="abs spine"></div>
    <div class="abs stripe"></div>
    <div class="abs photo-suit" role="img" aria-label="Photo of a lawyer in a dark suit holding a leather briefcase, head out of frame"></div>
    <div class="abs photo-paper" role="img" aria-label="Photo of a lawsuit document with a pen resting on it"></div>

    <div class="pill" style="left:218px;top:47px">Case Results</div>
    <div class="case-list">
      <div class="sub">Recent Case Results</div>
      <div class="case">
        <h4>Larceny (over $2500 but less than $20,000) and Conspiracy to Commit Larceny (over $2500 but less than $20,000) Client Faced 4 and ½ years in Jail</h4>
        Case Dismissed by prosecutor after our attorneys asked for Evidence related to the Offense that prosecutor was unable to provide.
      </div>
      <div class="case">
        <h4 style="font-family:'Noto Serif',serif;font-weight:700">8/20/13</h4>
        1st Degree Felony Kidnapping (Sexual Offense Comitted), Criminal Sexual Contact, Battery Against a Household Member (4 Counts) Client faced 23 and ½ years in Jail. All charges dismissed upon Prosecutor's failure to comply with Defense Council's Discovery Demands.
      </div>
      <div class="case">
        <h4 style="font-family:'Noto Serif',serif;font-weight:700">9/13/13</h4>
        DWI First Offense, Careless Driving, and Open Container-Client was involved in a roll over accident on the Freeway, blew a .08, .09. - Found not guilty at trial.
      </div>
      <div class="case">
        <h4>3rd Degree Felony ABANDONMENT OR ABUSE OF A CHILD 3 counts</h4>
        Client faced 9 years in jail if convicted. Client was acquitted of all Charges at Trial. Case dismissed and charges against co-defendant were dropped.
      </div>
    </div>

    <div class="pill" style="left:218px;top:444px">Contact US</div>
    <div class="contact-copy">If you have been arrested for any criminal offense, do not hesitate to contact our law offices.</div>

    <div class="abs map-card">
      <div class="map-area" role="img" aria-label="Street map showing the office location"></div>
      <span class="map-pin"></span>
      <div class="map-text">Piñon Ridge<br>Legal Team<br>2140 Cedar Lane NW,<br>Albuquerque,<br>NM 87102</div>
      <div class="map-phone">
        <svg width="12" height="12" viewBox="0 0 24 24" aria-hidden="true"><circle cx="12" cy="12" r="11" fill="none" stroke="#b49a62" stroke-width="2"/><path d="M8 6.5c.6-.5 1.4-.4 1.8.2l1 1.6c.3.5.2 1.1-.2 1.5l-.7.6c.6 1.4 1.600 2.5 3 3.1l.6-.7c.4-.4 1-.5 1.5-.2l1.6 1c.6.4.7 1.2.2 1.8l-.7.8c-.8.8-2 .9-3 .4-2.7-1.3-4.8-3.4-6.1-6.1-.5-1-.4-2.2.4-3z" fill="#b49a62"/></svg>
        505.555.0147
      </div>
    </div>
    <div class="web-back">www.pinonridgelegalteam.com</div>
  </section>
</body>
</html>
```